Corrigan Construction Law P.A.

Business Card with Corporate Logo. For a law firm specializing in construction law.

need address, telephone, email and website. Also, have an elegant and conservative logo.

Logo so it is RBN.

Full name "Gordon T. Corrigan

Under my name title "Attorney at Law"

Under title "Board Certified in Construction Law"

PA in email is lower case

Add logo to back side of card

Mix in a bit of gold color into card to go with the green

Some color on bottom
Updates

Target Market(s)

legal

Industry/Entity Type

Construction

Contact Information for Business Card

I like it -- edits: 1. add "L" to logo so it is RBN. 2. add my full name "Gordon T. Business Card with Corporate Logo. For a law firm specializing in construction law.

Logo so it is RBN.

PA in email is lower case

Font styles to use
Serif

Colors
00a990
f78f20

Requirements
Must have
• Conservative legal designed logo for construction market
• Address:
• Corrigan Construction Law, P.A.
• 4150 Meadowlark Ave North, Ste B4
• Jacksonville, Florida 32217
• Main: 904-555-3172
• Direct: 904-555-8410
• Fax: 904-555-8410
• gt@corriganpa-example.com
• www.corriganbuildlaw-example.com
Nice to have
• Catchy conservative logo on card
Should not have
• Flashy

```html
<!DOCTYPE html>
<html lang="en">
<head>
<meta charset="utf-8">
<title>Corrigan Construction Law – Business Cards</title>
<link rel="stylesheet" href="https://fonts.googleapis.com/css2?family=Libre+Baskerville:wght@400;700&display=swap">
<style>
  :root {
    --page-bg: #ecebe8;
    --card-white: #ffffff;
    --card-soft: #e9eae9;
    --brand-green: #00a990;
    --brand-green-deep: #00806d;
    --brand-gold: #f78f20;
    --gold-light: #fbc27f;
    --logo-ink: #00806d;
    --name-ink: #6f7172;
    --text-light: #ffffff;
    --text-soft: #e6f6f2;
    --shadow: rgba(0, 0, 0, 0.18);
  }
  * { margin: 0; padding: 0; box-sizing: border-box; }
  html, body {
    width: 1200px;
    height: 899px;
    overflow: hidden;
    background: var(--page-bg);
    font-family: "Libre Baskerville", Georgia, serif;
  }
  .canvas { position: relative; width: 1200px; height: 899px; }

  .card {
    position: absolute;
    width: 680px;
    height: 388px;
    overflow: hidden;
    box-shadow: 0 10px 28px var(--shadow);
  }

  /* Front card */
  .card-front {
    left: 170px;
    top: 40px;
    background: radial-gradient(ellipse at 50% 35%, var(--card-white) 0%, var(--card-soft) 100%);
    display: flex;
    flex-direction: column;
    align-items: center;
    justify-content: center;
  }
  .brand-mark {
    display: flex;
    align-items: center;
    gap: 14px;
  }
  .brand-dot {
    width: 20px;
    height: 20px;
    border-radius: 50%;
    background: var(--brand-gold);
  }
  .brand-initials {
    font-size: 60px;
    font-weight: 700;
    letter-spacing: 6px;
    color: var(--logo-ink);
    line-height: 1;
  }
  .firm-name {
    margin-top: 20px;
    font-size: 22px;
    font-weight: 400;
    color: var(--name-ink);
    letter-spacing: 0.5px;
  }

  /* Back card */
  .card-back {
    left: 350px;
    top: 468px;
    background: var(--card-white);
  }
  .back-art { position: absolute; inset: 0; }
  .holder {
    position: absolute;
    left: 32px;
    top: 30px;
    color: var(--text-light);
  }
  .holder-name { font-size: 20px; font-weight: 700; }
  .holder-title { font-size: 13px; color: var(--text-soft); margin-top: 5px; }
  .holder-cert { font-size: 11px; color: var(--text-soft); margin-top: 3px; font-style: italic; }

  .contact-list {
    position: absolute;
    left: 32px;
    bottom: 22px;
    list-style: none;
    color: var(--text-light);
    font-size: 11.5px;
    line-height: 19px;
  }
  .contact-list li { display: flex; align-items: flex-start; gap: 8px; }
  .contact-list svg { flex: none; margin-top: 4px; }
  .contact-address { line-height: 16px; margin-bottom: 4px; }
  .contact-label { color: var(--gold-light); }

  .back-logo {
    position: absolute;
    right: 62px;
    top: 160px;
  }
  .back-logo .brand-initials { font-size: 52px; }
  .back-logo .brand-dot { width: 16px; height: 16px; }
</style>
</head>
<body>
<main class="canvas">

  <section class="card card-front" aria-label="Business card front">
    <div class="brand-mark">
      <span class="brand-dot"></span>
      <span class="brand-initials">RBN</span>
    </div>
    <p class="firm-name">Corrigan Construction Law</p>
  </section>

  <section class="card card-back" aria-label="Business card back">
    <svg class="back-art" viewBox="0 0 680 388" width="680" height="388" aria-hidden="true">
      <defs>
        <linearGradient id="gold-swoosh" x1="0" y1="0" x2="1" y2="0">
          <stop offset="0" stop-color="#f78f20"/>
          <stop offset="1" stop-color="#fbc27f"/>
        </linearGradient>
      </defs>
      <path d="M0 0 H310 C260 40 236 110 260 180 C290 270 380 340 450 388 H0 Z" fill="url(#gold-swoosh)"/>
      <path d="M0 0 H292 C246 44 222 112 246 182 C274 266 360 336 424 388 H0 Z" fill="var(--brand-green)"/>
    </svg>

    <div class="holder">
      <p class="holder-name">Gordon T. Corrigan</p>
      <p class="holder-title">Attorney at Law</p>
      <p class="holder-cert">Board Certified in Construction Law</p>
    </div>

    <ul class="contact-list">
      <li class="contact-address">
        <svg width="10" height="10" viewBox="0 0 10 10"><path d="M5 1 L9 5 H8 V9 H2 V5 H1 Z" fill="#fff"/></svg>
        <span>Corrigan Construction Law, P.A.<br>4150 Meadowlark Ave North, Ste B4<br>Jacksonville, Florida 32217</span>
      </li>
      <li>
        <svg width="10" height="10" viewBox="0 0 10 10"><circle cx="5" cy="5" r="5" fill="#fff"/><path d="M3 2.5 L4.3 2.5 L4.6 4 L3.9 4.6 Q4.6 6 5.6 6.2 L6.1 5.5 L7.5 5.8 L7.5 7 Q4 7.4 3 2.5 Z" fill="#00a990"/></svg>
        <span><span class="contact-label">Main:</span> 904-555-3172</span>
      </li>
      <li>
        <svg width="10" height="10" viewBox="0 0 10 10"><circle cx="5" cy="5" r="5" fill="#fff"/><rect x="3.4" y="2" width="3.2" height="6" rx="0.6" fill="#00a990"/></svg>
        <span><span class="contact-label">Direct:</span> 904-555-8410</span>
      </li>
      <li>
        <svg width="10" height="10" viewBox="0 0 10 10"><circle cx="5" cy="5" r="5" fill="#fff"/><rect x="2.5" y="3" width="5" height="4" fill="#00a990"/></svg>
        <span><span class="contact-label">Fax:</span> 904-555-8410</span>
      </li>
      <li>
        <svg width="10" height="10" viewBox="0 0 10 10"><circle cx="5" cy="5" r="5" fill="#fff"/><path d="M2.5 3.2 H7.5 V6.8 H2.5 Z M2.5 3.2 L5 5.2 L7.5 3.2" fill="none" stroke="#00a990" stroke-width="0.8"/></svg>
        <span>gt@corriganpa-example.com</span>
      </li>
      <li>
        <svg width="10" height="10" viewBox="0 0 10 10"><circle cx="5" cy="5" r="5" fill="#fff"/><circle cx="5" cy="5" r="2.6" fill="none" stroke="#00a990" stroke-width="0.8"/><path d="M2.4 5 H7.6 M5 2.4 V7.6" stroke="#00a990" stroke-width="0.6"/></svg>
        <span>www.corriganbuildlaw-example.com</span>
      </li>
    </ul>

    <div class="brand-mark back-logo">
      <span class="brand-dot"></span>
      <span class="brand-initials">RBN</span>
    </div>
  </section>

</main>
</body>
</html>
```